Logo, letterhead and business card for new counseling business

Looking for a clean and professional design. The name of the business is Clearwater Counseling, PLLC with a website of www.clearwatercounselingmn.example We specialize in working with adolescents and families. We are looking for a logo that exudes confidence, trust, hope, compassion. I am excited to open my new business and help families get better, overcome their issues and enjoy their lives more. I have spent the past 9 years working for others and it is time for me to make my own way. I have strong ethics so people can trust me. I care for the people I serve. I need a logo to go along with my strong business name to help me stand out even though I am just starting my business.

Target Market(s)

Adolescent and families who are struggling emotionally or have addiction issues.

Industry/Entity Type

Business

Contact Information for Business Card

Clearwater Counseling, PLLC
48215 Larkspur Avenue, Suite 310, Maple Grove, Minnesota, 55369
(612)555-0147
dana@clearwatercounselingmn.example
clearwatercounselingmn.example

Logo Text

Clearwater Counseling

Logo styles of interest
Emblem Logo
Pictorial/Combination Logo
Wordmark Logo
Font styles to use
Serif
Sans Serif

Requirements
Must have
• Clean, professional design.
Nice to have
• I want the design to feel trustworthy and safe. Dependable.
Should not have
• childish fonts

```html
<!DOCTYPE html>
<html lang="en">
<head>
<meta charset="utf-8">
<title>Clearwater Counseling — Stationery</title>
<link href="https://fonts.googleapis.com/css2?family=Lato:wght@300;400;700&display=swap" rel="stylesheet">
<style>
  :root{
    --bg:#e6e7e9;
    --paper:#ffffff;
    --ink:#2b2b2b;
    --muted:#555a60;
    --navy:#1e3a52;
    --black:#0b0b0b;
    --blue:#2b93d6;
    --orange:#f28a22;
    --red:#d4104c;
    --green:#72b62a;
    --slot:#e4e4e4;
    --faint:#cfcfcf;
  }
  *{box-sizing:border-box;margin:0;padding:0}
  html,body{width:1200px;height:2359px;overflow:hidden}
  body{background:var(--bg);position:relative;font-family:"Lato",Arial,sans-serif;color:var(--ink)}
  .piece{position:absolute;box-shadow:4px 10px 14px rgba(0,0,0,.28)}

  /* wordmark */
  .wordmark{display:flex;align-items:center;gap:12px;font-weight:300;color:var(--ink);white-space:nowrap}
  .wordmark .dot{border-radius:50%;background:var(--blue);flex:none}
  .wordmark.light{color:#fff}

  /* letterhead */
  .letterhead{left:57px;top:39px;width:519px;height:732px;background:var(--paper)}
  .letterhead .wordmark{position:absolute;left:60px;top:74px;font-size:24px}
  .letterhead .wordmark .dot{width:26px;height:26px}
  .letter-body{position:absolute;left:69px;top:174px;width:428px;font-size:8.4px;line-height:12.4px;color:#333}
  .letter-body p{margin-bottom:12px}
  .sign-area{width:60px;height:26px;background:#f1f1f1;margin-top:14px}
  .letter-contact{position:absolute;right:30px;top:548px;text-align:right;font-size:8.4px;line-height:12px;color:#333}
  .letter-contact .row{display:flex;justify-content:flex-end;align-items:flex-start;gap:8px;margin-bottom:10px}
  .letter-contact svg{width:10px;height:10px;flex:none;margin-top:1px}
  .color-bar{position:absolute;left:0;right:0;bottom:0;height:9px;display:flex}
  .color-bar span{flex:1}

  /* cover */
  .cover{left:626px;top:39px;width:517px;height:733px;background:linear-gradient(160deg,#1c1c1c,#000 60%)}
  .cover .wordmark{position:absolute;left:42px;top:340px;font-size:36px}
  .cover .wordmark .dot{width:40px;height:40px}

  /* cards */
  .card{top:845px;width:522px;height:307px;border-radius:40px}
  .card-front{left:47px;background:var(--paper)}
  .card-front .wordmark{position:absolute;left:74px;top:132px;font-size:30px}
  .card-front .wordmark .dot{width:34px;height:34px}
  .card-back{left:623px;background:linear-gradient(160deg,#222,#050505 70%);color:#fff;overflow:hidden}
  .card-back .wordmark{position:absolute;left:30px;top:132px;font-size:22px;flex-direction:column;align-items:flex-start;gap:10px}
  .card-back .wordmark .dot{width:40px;height:40px}
  .card-name{position:absolute;right:36px;top:76px;text-align:right}
  .card-name h2{font-weight:400;font-size:24px;letter-spacing:.5px}
  .card-name small{font-size:11px;letter-spacing:.5px}
  .card-contact{position:absolute;right:30px;top:150px;text-align:right;font-size:11px;line-height:14px}
  .card-contact .row{display:flex;justify-content:flex-end;align-items:flex-start;gap:10px;margin-bottom:8px}
  .card-contact svg{width:11px;height:11px;flex:none;margin-top:1px}

  /* envelopes */
  .envelope{left:102px;width:982px;background:var(--paper)}
  .env-front{top:1326px;height:448px}
  .env-front-flap{position:absolute;left:102px;top:1241px;width:982px;height:86px}
  .env-front .wordmark{position:absolute;left:50px;top:82px;font-size:34px}
  .env-front .wordmark .dot{width:38px;height:38px}
  .env-contact{position:absolute;left:50px;top:218px;font-size:18px;line-height:24px;color:var(--navy)}
  .env-contact .row{display:flex;align-items:flex-start;gap:22px;margin-bottom:12px}
  .env-contact svg{width:18px;height:18px;flex:none;margin-top:3px}
  .address-window{position:absolute;left:516px;top:193px;width:373px;height:153px;background:var(--slot)}
  .env-back{left:110px;top:1816px;height:457px}
  .env-back-flap{position:absolute;left:0;top:0;width:982px;height:84px}
  .env-back .wordmark{position:absolute;left:0;right:0;top:208px;justify-content:center;font-size:30px;color:var(--faint)}
  .env-back .wordmark .dot{width:34px;height:34px;background:var(--faint)}
</style>
</head>
<body>

<!-- Letterhead -->
<section class="piece letterhead">
  <div class="wordmark"><span class="dot"></span>Clearwater Counseling</div>
  <div class="letter-body">
    <p>Dear Friend,</p>
    <p>Lorem ipsum dolor sit amet, consectetur adipisicing elit, sed do eiusmod tempor incididunt ut labore et dolore magna aliqua. Ut enim ad minim veniam, quis nostrud exercitation ullamco laboris nisi ut aliquip ex ea commodo consequat. Duis aute irure dolor in reprehenderit in voluptate velit esse cillum dolore eu fugiat nulla pariatur. Excepteur sint occaecat cupidatat non proident, sunt in culpa qui officia deserunt mollit anim id est laborum.</p>
    <p>Duis aute irure dolor in reprehenderit in voluptate velit esse cillum dolore eu fugiat nulla pariatur. Excepteur sint occaecat cupidatat non proident. Lorem ipsum dolor sit amet, consectetur adipisicing elit, sed do eiusmod tempor incididunt ut labore et dolore magna aliqua. Ut enim ad minim veniam, quis nostrud exercitation ullamco laboris nisi ut aliquip ex ea commodo consequat. Duis aute irure dolor in reprehenderit in voluptate velit esse cillum dolore eu fugiat nulla pariatur. Excepteur sint occaecat cupidatat non proident, sed do eiusmod tempor incididunt ut labore et dolore magna aliqua. Ut enim ad minim veniam, quis nostrud exercitation ullamco laboris nisi ut aliquip ex ea commodo consequat.</p>
    <p>Excepteur sint occaecat cupidatat non proident, sunt in culpa qui officia deserunt mollit anim id est laborum. Lorem ipsum dolor sit amet, consectetur adipisicing elit, sed do eiusmod tempor incididunt ut labore et dolore magna aliqua.</p>
    <p>Best Regards,</p>
    <p style="margin-bottom:0">Dana Morrow</p>
    <div class="sign-area" role="img" aria-label="Handwritten signature"></div>
  </div>
  <div class="letter-contact">
    <div class="row"><span>48215 Larkspur Avenue, Suite 310<br>Maple Grove, MN 55369</span>
      <svg viewBox="0 0 10 10"><path d="M5 0a3.5 3.5 0 0 0-3.5 3.5C1.5 6 5 10 5 10s3.5-4 3.5-6.5A3.5 3.5 0 0 0 5 0zm0 5a1.4 1.4 0 1 1 0-2.8A1.4 1.4 0 0 1 5 5z" fill="var(--blue)"/></svg></div>
    <div class="row"><span>(612)555-0147<br>0000 - 00 000</span>
      <svg viewBox="0 0 10 10"><path d="M1 3c0-1 1-2 4-2s4 1 4 2v1H7V3H3v1H1zM2 5h6l1 4H1z" fill="var(--orange)"/></svg></div>
    <div class="row"><span>hello@clearwatercounselingmn.example<br>www.clearwatercounselingmn.example</span>
      <svg viewBox="0 0 10 10"><rect x="0.5" y="1.5" width="9" height="6" fill="var(--green)"/><circle cx="5" cy="8.5" r="0" fill="none"/></svg></div>
  </div>
  <div class="color-bar"><span style="background:var(--blue)"></span><span style="background:var(--orange)"></span><span style="background:var(--red)"></span><span style="background:var(--green)"></span></div>
</section>

<!-- Cover -->
<section class="piece cover">
  <div class="wordmark light"><span class="dot"></span>Clearwater Counseling</div>
</section>

<!-- Business card front -->
<section class="piece card card-front">
  <div class="wordmark"><span class="dot"></span>Clearwater Counseling</div>
</section>

<!-- Business card back -->
<section class="piece card card-back">
  <div class="wordmark light"><span class="dot"></span>Clearwater<br>Counseling</div>
  <div class="card-name"><h2>YOUR NAME</h2><small>LEADER</small></div>
  <div class="card-contact">
    <div class="row"><span>48215 Larkspur Ave<br>Maple Grove, MN 55369</span>
      <svg viewBox="0 0 10 10"><path d="M5 0a3.5 3.5 0 0 0-3.5 3.5C1.5 6 5 10 5 10s3.5-4 3.5-6.5A3.5 3.5 0 0 0 5 0zm0 5a1.4 1.4 0 1 1 0-2.8A1.4 1.4 0 0 1 5 5z" fill="var(--blue)"/></svg></div>
    <div class="row"><span>(612)555-0147</span>
      <svg viewBox="0 0 10 10"><path d="M1 3c0-1 1-2 4-2s4 1 4 2v1H7V3H3v1H1zM2 5h6l1 4H1z" fill="var(--orange)"/></svg></div>
    <div class="row"><span>0000 - 00 000</span>
      <svg viewBox="0 0 10 10"><path d="M1 3c0-1 1-2 4-2s4 1 4 2v1H7V3H3v1H1zM2 5h6l1 4H1z" fill="var(--red)"/></svg></div>
    <div class="row"><span>dana@clearwatercounselingmn.example</span>
      <svg viewBox="0 0 10 10"><rect x="0.5" y="2" width="9" height="6" fill="var(--green)"/><path d="M0.5 2L5 5.5 9.5 2" stroke="#111" stroke-width="0.8" fill="none"/></svg></div>
    <div class="row"><span>www.clearwatercounselingmn.example</span>
      <svg viewBox="0 0 10 10"><circle cx="5" cy="5" r="4.5" fill="var(--blue)"/></svg></div>
  </div>
</section>

<!-- Envelope front -->
<svg class="env-front-flap" viewBox="0 0 982 86" preserveAspectRatio="none" aria-hidden="true">
  <defs><linearGradient id="flapA" x1="0" y1="0" x2="0" y2="1"><stop offset="0" stop-color="#000"/><stop offset="1" stop-color="#2a2a2a"/></linearGradient></defs>
  <polygon points="55,0 928,0 982,86 0,86" fill="url(#flapA)"/>
</svg>
<section class="piece envelope env-front">
  <div class="wordmark"><span class="dot"></span>Clearwater Counseling</div>
  <div class="env-contact">
    <div class="row"><svg viewBox="0 0 10 10"><path d="M5 0a3.5 3.5 0 0 0-3.5 3.5C1.5 6 5 10 5 10s3.5-4 3.5-6.5A3.5 3.5 0 0 0 5 0zm0 5a1.4 1.4 0 1 1 0-2.8A1.4 1.4 0 0 1 5 5z" fill="var(--blue)"/></svg>
      <span>48215 Larkspur Avenue, Suite 310<br>Maple Grove, MN 55369</span></div>
    <div class="row"><svg viewBox="0 0 10 10"><path d="M1 3c0-1 1-2 4-2s4 1 4 2v1H7V3H3v1H1zM2 5h6l1 4H1z" fill="var(--orange)"/></svg>
      <span>(612)555-0147</span></div>
    <div class="row"><svg viewBox="0 0 10 10"><rect x="0.5" y="2" width="9" height="6" fill="var(--red)"/><path d="M0.5 2L5 5.5 9.5 2" stroke="#fff" stroke-width="0.8" fill="none"/></svg>
      <span>hello@clearwatercounselingmn.example</span></div>
    <div class="row"><svg viewBox="0 0 10 10"><circle cx="5" cy="5" r="4.5" fill="var(--green)"/><path d="M0.5 5h9M5 0.5v9" stroke="#fff" stroke-width="0.7"/></svg>
      <span>www.clearwatercounselingmn.example</span></div>
  </div>
  <div class="address-window"></div>
</section>

<!-- Envelope back -->
<section class="piece envelope env-back">
  <svg class="env-back-flap" viewBox="0 0 982 84" preserveAspectRatio="none" aria-hidden="true">
    <defs><linearGradient id="flapB" x1="0" y1="0" x2="0" y2="1"><stop offset="0" stop-color="#000"/><stop offset="1" stop-color="#2a2a2a"/></linearGradient></defs>
    <polygon points="0,0 982,0 920,84 55,84" fill="url(#flapB)"/>
  </svg>
  <div class="wordmark"><span class="dot"></span>Clearwater Counseling</div>
</section>

</body>
</html>
```